Business Card Design Project

Hi. We need a new business card for Brightfield Partners, a consultancy that helps people with online marketing strategy and solutions.

We have a new logo and now need the info presented - front and back of business card.

FRONT

Logo

Online strategy, consulting and coaching
Varlo Admarket consulting
Search Engine Optimisation
Internet Lead Generation
Domain name broking

BACK

Tom Bradwell-Jones
+ 61 83215 9076
+ 61 (0) 418 536 207
tom@brightfieldpartners.com.au
www.brightfieldpartners.com.au

Talkora: tombradwelljones
PO Box 312, South Perth, Western Australia 6951

Target Market(s)

Business owners, corporates

Industry/Entity Type

Marketing

Requirements
Must have
• double sided
size: 86 x 54mm
supplied as one pdf with crop marks shown (+- 1mm, with 2-3 mm bleed)

```html
<!DOCTYPE html>
<html lang="en">
<head>
<meta charset="utf-8">
<title>Brightfield Partners – Business Card Set</title>
<link href="https://fonts.googleapis.com/css2?family=Open+Sans:wght@400;700;800&family=PT+Sans&display=swap" rel="stylesheet">
<style>
  :root{
    --stage:#e9e4dc;
    --card-white:#ffffff;
    --card-black:#231f20;
    --card-blue:#1f4f95;
    --card-blue-light:#2a63ad;
    --brand-blue:#1d4f91;
    --brand-orange:#f7941d;
    --ink:#333333;
    --label:#1a1a1a;
    --white:#ffffff;
  }
  *{box-sizing:border-box;margin:0;padding:0}
  html,body{width:1200px;height:788px;overflow:hidden}
  body{background:var(--stage);position:relative;font-family:"Open Sans",Arial,sans-serif}

  .side-label{position:absolute;font-family:"PT Sans",Arial,sans-serif;font-size:22px;color:var(--label);transform:translateX(-50%)}

  .card{position:absolute;width:508px;height:319px;border-radius:18px;overflow:hidden;box-shadow:0 3px 8px rgba(0,0,0,.35)}
  .card--back{left:70px;top:48px;background:var(--card-white)}
  .card--front-1{left:639px;top:48px;background:var(--card-white)}
  .card--front-2{left:70px;top:436px;background:var(--card-black)}
  .card--front-3{left:639px;top:436px;background:linear-gradient(90deg,var(--card-blue) 0%,var(--card-blue-light) 100%)}

  /* brand lockup */
  .brand{position:absolute;display:flex;flex-direction:column;align-items:center}
  .brand__row{display:flex;align-items:center;gap:14px}
  .brand__dot{border-radius:50%;background:var(--brand-orange);flex:none}
  .brand__name{font-weight:800;line-height:.95;letter-spacing:-.5px}
  .brand__url{font-weight:700;letter-spacing:2.4px;margin-top:8px}

  .card--back .brand{left:28px;top:72px}
  .card--back .brand__dot{width:40px;height:40px}
  .card--back .brand__name{font-size:27px;color:var(--brand-blue)}
  .card--back .brand__url{font-size:8px;letter-spacing:1.2px;color:var(--brand-blue);margin-top:6px}

  .card--front-1 .brand,.card--front-2 .brand,.card--front-3 .brand{left:0;right:0;top:36px}
  .brand--large .brand__dot{width:78px;height:78px}
  .brand--large .brand__name{font-size:50px}
  .brand--large .brand__url{font-size:12px}
  .card--front-1 .brand__name,.card--front-1 .brand__url{color:var(--brand-blue)}
  .card--front-2 .brand__name,.card--front-2 .brand__url,
  .card--front-3 .brand__name,.card--front-3 .brand__url{color:var(--white)}

  /* back details */
  .divider{position:absolute;left:253px;top:62px;width:2px;height:120px;background:#b5b5b5}
  .contact{position:absolute;left:273px;top:62px;font-size:12.5px;color:var(--ink);line-height:20px;list-style:none}
  .contact__name{font-size:17px;font-weight:700;line-height:24px;margin-bottom:1px}
  .contact b{font-weight:700}
  .wave{position:absolute;left:0;top:0}
  .address{position:absolute;left:45px;top:270px;color:var(--white);font-size:12.5px;line-height:17px}

  /* services */
  .services{list-style:none;position:absolute}
  .card--front-1 .services{left:139px;top:210px;color:var(--brand-blue);font-size:12.5px;line-height:19.5px}
  .card--front-1 .services li{display:flex;align-items:center;gap:8px}
  .bullet-dot{width:11px;height:11px;border-radius:50%;background:var(--brand-orange);flex:none}

  .services--grid{left:0;right:0;top:228px;color:var(--white);font-size:12.5px;display:grid;grid-template-columns:205px 205px;justify-content:center;row-gap:7px;padding-left:36px}
  .services--grid li::before{content:"";display:inline-block;width:4px;height:4px;background:var(--white);margin-right:5px;vertical-align:middle}
  .services--grid .services__lead{grid-column:1 / 3;text-align:center;padding-right:36px}
</style>
</head>
<body>

<span class="side-label" style="left:318px;top:16px">back</span>
<span class="side-label" style="left:897px;top:16px">front - 1</span>
<span class="side-label" style="left:325px;top:404px">front - 2</span>
<span class="side-label" style="left:897px;top:404px">front - 3</span>

<!-- Back -->
<section class="card card--back">
  <svg class="wave" width="508" height="319" viewBox="0 0 508 319" aria-hidden="true">
    <path d="M110,238 C220,224 300,262 370,272 C430,280 480,258 508,238 L508,246 C480,268 430,288 370,282 C300,272 220,236 110,238Z" fill="var(--brand-orange)"/>
    <path d="M0,252 C70,236 150,234 230,250 C300,264 350,290 420,288 C460,287 490,265 508,252 V319 H0Z" fill="var(--brand-blue)"/>
  </svg>
  <div class="brand">
    <div class="brand__row">
      <span class="brand__dot"></span>
      <span class="brand__name">Brightfield<br>Partners</span>
    </div>
    <span class="brand__url">brightfieldpartners.com.au</span>
  </div>
  <div class="divider"></div>
  <ul class="contact">
    <li class="contact__name">Tom Bradwell-Jones</li>
    <li><b>p</b> : + 61 83215 9076</li>
    <li><b>c</b> : + 61 (0) 418 536 207</li>
    <li><b>talkora</b> : tombradwelljones</li>
    <li><b>e</b> : tom@brightfieldpartners.com.au</li>
    <li><b>w</b> : www.brightfieldpartners.com.au</li>
  </ul>
  <p class="address">PO Box 312, South Perth<br>Western Australia 6951</p>
</section>

<!-- Front 1 -->
<section class="card card--front-1">
  <div class="brand brand--large">
    <div class="brand__row">
      <span class="brand__dot"></span>
      <span class="brand__name">Brightfield<br>Partners</span>
    </div>
    <span class="brand__url">brightfieldpartners.com.au</span>
  </div>
  <ul class="services">
    <li><span class="bullet-dot"></span>Online strategy, consulting and coaching</li>
    <li><span class="bullet-dot"></span>Varlo Admarket consulting</li>
    <li><span class="bullet-dot"></span>Search Engine Optimisation</li>
    <li><span class="bullet-dot"></span>Internet Lead Generation</li>
    <li><span class="bullet-dot"></span>Domain name broking</li>
  </ul>
</section>

<!-- Front 2 -->
<section class="card card--front-2">
  <div class="brand brand--large">
    <div class="brand__row">
      <span class="brand__dot"></span>
      <span class="brand__name">Brightfield<br>Partners</span>
    </div>
    <span class="brand__url">brightfieldpartners.com.au</span>
  </div>
  <ul class="services services--grid">
    <li class="services__lead">Online strategy, consulting and coaching</li>
    <li>Varlo Admarket consulting</li>
    <li>Search Engine Optimisation</li>
    <li>Internet Lead Generation</li>
    <li>Domain name broking</li>
  </ul>
</section>

<!-- Front 3 -->
<section class="card card--front-3">
  <div class="brand brand--large">
    <div class="brand__row">
      <span class="brand__dot"></span>
      <span class="brand__name">Brightfield<br>Partners</span>
    </div>
    <span class="brand__url">brightfieldpartners.com.au</span>
  </div>
  <ul class="services services--grid">
    <li class="services__lead">Online strategy, consulting and coaching</li>
    <li>Varlo Admarket consulting</li>
    <li>Search Engine Optimisation</li>
    <li>Internet Lead Generation</li>
    <li>Domain name broking</li>
  </ul>
</section>

</body>
</html>
```